Skip Bin Hire Business

We are an existing business that hire out skip bins for domestic and commercial use. We are looking for a fresh look with no colours or designs in mind.
We have 2m3 and 3m3 skip bins and 3m3 up to 24m3 walk in bins.
Visit our website for more information.
www.harborcrate.com.au
We are going to add a photo of a 3m3 skip as this is a new product for our company and not available on our website at this stage.

Industry/Entity Type

Business

Contact Information for Business Card

Harbor Crate
9172-4086
www.harborcrate.com.au

```html
<!DOCTYPE html>
<html lang="en">
<head>
<meta charset="utf-8">
<title>Harbor Crate – Business Card</title>
<link href="https://fonts.googleapis.com/css2?family=Archivo+Black&display=swap" rel="stylesheet">
<style>
  :root {
    --page-bg: #e6e8ec;
    --card-gold: #e0a11e;
    --band-black: #151515;
    --band-red: #9a1a10;
    --ink-dark: #1c1c1c;
    --white: #ffffff;
  }
  * { margin: 0; padding: 0; box-sizing: border-box; }
  html, body {
    width: 1200px;
    height: 960px;
    overflow: hidden;
    background: var(--page-bg);
  }
  .stage {
    width: 1200px;
    height: 960px;
    display: flex;
    align-items: center;
    justify-content: center;
  }
  .business-card {
    position: relative;
    width: 900px;
    height: 514px;
    background: var(--card-gold);
    overflow: hidden;
    box-shadow: 0 10px 30px rgba(0,0,0,0.18);
  }
  .name-band {
    position: absolute;
    left: 0;
    top: 40px;
    width: 100%;
    height: 132px;
    background: var(--band-black);
    display: flex;
    align-items: center;
    justify-content: center;
  }
  .business-name {
    font-family: "Archivo Black", sans-serif;
    font-weight: 400;
    font-size: 78px;
    color: var(--white);
    letter-spacing: 2px;
    line-height: 1;
    white-space: nowrap;
  }
  .phone-block {
    position: absolute;
    top: 198px;
    left: 0;
    width: 100%;
    display: flex;
    flex-direction: column;
    align-items: center;
  }
  .phone-icon { width: 56px; height: 56px; }
  .phone-number {
    margin-top: 10px;
    font-family: "Archivo Black", sans-serif;
    font-size: 40px;
    line-height: 1.1;
    color: var(--ink-dark);
    letter-spacing: 1px;
  }
  .web-band {
    position: absolute;
    left: 0;
    top: 350px;
    width: 100%;
    height: 66px;
    background: var(--band-red);
    display: flex;
    align-items: center;
    justify-content: center;
  }
  .web-band::before,
  .web-band::after {
    content: "";
    position: absolute;
    left: 0;
    width: 100%;
    height: 3px;
    background: var(--white);
  }
  .web-band::before { top: 6px; }
  .web-band::after { bottom: 6px; }
  .web-address {
    font-family: "Archivo Black", sans-serif;
    font-size: 34px;
    line-height: 1;
    color: var(--white);
    letter-spacing: 1px;
    white-space: nowrap;
  }
  .tagline {
    position: absolute;
    top: 432px;
    left: 0;
    width: 100%;
    text-align: center;
    font-family: "Archivo Black", sans-serif;
    font-size: 36px;
    line-height: 1.1;
    color: var(--ink-dark);
    letter-spacing: 2px;
    white-space: nowrap;
  }
</style>
</head>
<body>
<main class="stage">
  <article class="business-card">
    <header class="name-band">
      <h1 class="business-name">Harbor Crate</h1>
    </header>

    <section class="phone-block">
      <svg class="phone-icon" viewBox="0 0 58 58" aria-hidden="true">
        <circle cx="29" cy="29" r="28" fill="var(--ink-dark)"/>
        <path d="M19 17c2-2 4-2 5 0l3 5c1 2 0 3-1 4l-2 1c1 3 4 7 8 9l1-2c1-1 2-2 4-1l5 3c2 1 2 3 0 5-3 3-7 3-12 0-6-4-11-10-13-16-1-4 0-6 2-8z" fill="var(--white)"/>
      </svg>
      <p class="phone-number">9172-4086</p>
    </section>

    <div class="web-band">
      <p class="web-address">www.harborcrate.com.au</p>
    </div>

    <p class="tagline">simple waste management</p>
  </article>
</main>
</body>
</html>
```